Business Card for Start-Up Consulting Business
TK Advisory Partners, LLC
Business Card for Start-Up Consulting Business - Consulting
Creative Brief
Professional
Roderick Lyle Pemberton
President/CEO
82 Fenwhistle Court #2410 Dover, DE 19906
info@tkapllc.example
www.tkapllc.example
On the back of the card, I would like something like: Text TKTEAM to 38217 for updates and promotions or For updates and promotions, text TKTEAM to 38217. I would also like to have our services listed on the back of the card like: We Specialize In: or Our Services Includes: *Negative Equity Financing *Tax Mitigation *Life & Health Insurance *Merchant Processing *Telecommunications *Energy Saving Programs *Marketing & Advertising and *More. And if the back is not crowded, maybe we can added the phone, fax, email and/or web address. Thanks

```html
<!DOCTYPE html>
<html lang="en">
<head>
<meta charset="utf-8">
<title>TK Advisory Partners, LLC — Business Card</title>
<link href="https://fonts.googleapis.com/css2?family=Cinzel:wght@400;600;700&family=Open+Sans:wght@400;600&family=Amiri&display=swap" rel="stylesheet">
<style>
  :root {
    --bg: #e6e7ea;
    --card: #ffffff;
    --navy: #1f4f8c;
    --green: #5aa83a;
    --ink: #2b2f36;
    --muted: #6a7078;
    --white: #ffffff;
  }
  * { box-sizing: border-box; margin: 0; padding: 0; }
  html, body { width: 1200px; height: 864px; overflow: hidden; }
  body {
    background: var(--bg);
    font-family: "Open Sans", sans-serif;
    position: relative;
  }
  .card {
    position: absolute;
    left: 270px;
    width: 660px;
    height: 377px;
    background: var(--card);
    border-radius: 18px;
    box-shadow: 0 6px 18px rgba(0,0,0,0.18);
    overflow: hidden;
  }
  .card--front { top: 36px; }
  .card--back { top: 451px; }

  /* Front: name mark, web address, services */
  .front-mark {
    position: absolute;
    top: 92px; left: 0; right: 0;
    display: flex; justify-content: center; align-items: center; gap: 14px;
  }
  .front-mark__square { width: 34px; height: 34px; background: var(--navy); }
  .front-mark__name {
    font-family: "Cinzel", serif;
    font-weight: 700;
    font-size: 30px;
    color: var(--navy);
    letter-spacing: 1px;
  }
  .front-web {
    position: absolute;
    top: 160px; left: 0; right: 0;
    text-align: center;
    font-family: "Cinzel", serif;
    font-size: 13px;
    letter-spacing: 7px;
    color: var(--muted);
    text-transform: uppercase;
  }
  .services {
    position: absolute;
    top: 212px; left: 60px; right: 60px;
    text-align: center;
  }
  .services__heading {
    font-family: "Cinzel", serif;
    font-weight: 600;
    font-size: 13px;
    color: var(--green);
    letter-spacing: 1px;
    margin-bottom: 8px;
  }
  .services__list {
    list-style: none;
    display: flex; flex-wrap: wrap; justify-content: center;
    gap: 5px 16px;
    font-size: 11.5px;
    color: var(--ink);
  }
  .services__list li::before {
    content: "";
    display: inline-block;
    width: 5px; height: 5px;
    background: var(--navy);
    margin-right: 6px;
    vertical-align: middle;
  }
  .text-offer {
    position: absolute;
    top: 318px; left: 0; right: 0;
    text-align: center;
    font-size: 12px;
    color: var(--navy);
  }
  .text-offer strong { font-weight: 600; }

  /* Back: identity and contact panel */
  .back-swoosh { position: absolute; inset: 0; }
  .back-identity {
    position: absolute;
    left: 40px; top: 56px;
    width: 400px;
  }
  .back-identity__blessing {
    font-family: "Amiri", serif;
    font-size: 15px;
    color: var(--navy);
    direction: rtl;
    text-align: left;
    margin-left: 70px;
    margin-bottom: 2px;
  }
  .back-identity__row { display: flex; align-items: center; gap: 12px; }
  .back-identity__square { width: 40px; height: 40px; background: var(--navy); flex: none; }
  .back-identity__company {
    font-family: "Cinzel", serif;
    font-weight: 700;
    font-size: 18px;
    color: var(--navy);
    line-height: 1.1;
    white-space: nowrap;
  }
  .back-identity__tagline {
    font-family: "Cinzel", serif;
    font-size: 10px;
    letter-spacing: 1.5px;
    color: var(--green);
    margin-top: 4px;
  }
  .back-person {
    position: absolute;
    left: 40px; top: 250px;
  }
  .back-person__name {
    font-family: "Cinzel", serif;
    font-weight: 600;
    font-size: 17px;
    color: var(--navy);
  }
  .back-person__title {
    font-family: "Cinzel", serif;
    font-size: 12px;
    color: var(--muted);
    margin-top: 2px;
  }
  .contact-list {
    position: absolute;
    left: 480px; top: 78px;
    list-style: none;
    display: flex; flex-direction: column; gap: 9px;
  }
  .contact-list__item {
    display: flex; align-items: center; gap: 8px;
    color: var(--white);
    font-size: 12px;
    line-height: 1.35;
  }
  .contact-list__icon {
    width: 16px; height: 16px; border-radius: 50%;
    background: var(--white);
    display: flex; align-items: center; justify-content: center;
    flex: none;
  }
</style>
</head>
<body>

<section class="card card--front" aria-label="Card front">
  <div class="front-mark">
    <span class="front-mark__square"></span>
    <span class="front-mark__name">TK Advisory Partners</span>
  </div>
  <p class="front-web">www.tkapllc.example</p>
  <div class="services">
    <p class="services__heading">We Specialize In:</p>
    <ul class="services__list">
      <li>Negative Equity Financing</li>
      <li>Tax Mitigation</li>
      <li>Life &amp; Health Insurance</li>
      <li>Merchant Processing</li>
      <li>Telecommunications</li>
      <li>Energy Saving Programs</li>
      <li>Marketing &amp; Advertising</li>
      <li>More</li>
    </ul>
  </div>
  <p class="text-offer">For updates and promotions, text <strong>TKTEAM</strong> to <strong>38217</strong></p>
</section>

<section class="card card--back" aria-label="Card back">
  <svg class="back-swoosh" width="660" height="377" viewBox="0 0 660 377" aria-hidden="true">
    <path d="M520 0 C 400 70, 360 230, 300 377 L 660 377 L 660 0 Z" fill="#5aa83a"/>
    <path d="M532 0 C 418 74, 380 230, 322 377 L 660 377 L 660 0 Z" fill="#ffffff"/>
    <path d="M540 0 C 430 78, 392 232, 336 377 L 660 377 L 660 0 Z" fill="#1f4f8c"/>
    <path d="M0 335 C 160 330, 260 320, 336 300" stroke="#5aa83a" stroke-width="3" fill="none"/>
    <path d="M0 348 C 170 344, 270 334, 336 318" stroke="#1f4f8c" stroke-width="6" fill="none"/>
  </svg>

  <div class="back-identity">
    <p class="back-identity__blessing">بسم الله الرحمن الرحيم</p>
    <div class="back-identity__row">
      <span class="back-identity__square"></span>
      <div>
        <p class="back-identity__company">TK Advisory Partners, LLC</p>
        <p class="back-identity__tagline">HELPING BUSINESSES GROW</p>
      </div>
    </div>
  </div>

  <div class="back-person">
    <p class="back-person__name">Roderick Lyle Pemberton</p>
    <p class="back-person__title">President/CEO</p>
  </div>

  <ul class="contact-list">
    <li class="contact-list__item">
      <span class="contact-list__icon"><svg width="10" height="10" viewBox="0 0 10 10"><path d="M2 1 L4 1 L4.6 3 L3.5 3.8 C4 5 5 6 6.2 6.5 L7 5.4 L9 6 L9 8 C5 8.5 1.5 5 2 1 Z" fill="#1f4f8c"/></svg></span>
      (302) 555-0148
    </li>
    <li class="contact-list__item">
      <span class="contact-list__icon"><svg width="10" height="10" viewBox="0 0 10 10"><path d="M2 1 L4 1 L4.6 3 L3.5 3.8 C4 5 5 6 6.2 6.5 L7 5.4 L9 6 L9 8 C5 8.5 1.5 5 2 1 Z" fill="#1f4f8c"/></svg></span>
      (302) 555-0176
    </li>
    <li class="contact-list__item">
      <span class="contact-list__icon"><svg width="10" height="10" viewBox="0 0 10 10"><rect x="1.5" y="3" width="7" height="4.5" fill="#1f4f8c"/><rect x="3" y="1" width="4" height="2" fill="#1f4f8c"/></svg></span>
      (888) 555-0192
    </li>
    <li class="contact-list__item">
      <span class="contact-list__icon"><svg width="10" height="10" viewBox="0 0 10 10"><rect x="1" y="2.5" width="8" height="5.5" fill="none" stroke="#1f4f8c" stroke-width="1"/><path d="M1 2.5 L5 5.5 L9 2.5" fill="none" stroke="#1f4f8c" stroke-width="1"/></svg></span>
      info@tkapllc.example
    </li>
    <li class="contact-list__item">
      <span class="contact-list__icon"><svg width="10" height="10" viewBox="0 0 10 10"><circle cx="5" cy="5" r="3.8" fill="none" stroke="#1f4f8c" stroke-width="1"/><path d="M1.2 5 H8.8 M5 1.2 C3 3.5 3 6.5 5 8.8 M5 1.2 C7 3.5 7 6.5 5 8.8" fill="none" stroke="#1f4f8c" stroke-width="0.8"/></svg></span>
      www.tkapllc.example
    </li>
    <li class="contact-list__item">
      <span class="contact-list__icon"><svg width="10" height="10" viewBox="0 0 10 10"><path d="M5 9 C3 6.5 2 5 2 3.8 A3 3 0 0 1 8 3.8 C8 5 7 6.5 5 9 Z" fill="#1f4f8c"/><circle cx="5" cy="3.8" r="1.1" fill="#ffffff"/></svg></span>
      <span>82 Fenwhistle Court #2410<br>Dover, DE 19906</span>
    </li>
  </ul>
</section>

</body>
</html>
```